I'm looking for a fresh new design for my business Martin Coldwell Creative.
I am a photographer and videographer.
The card must be easy to print, eye catching and easy to read. It must reflect the fact that I work in a creative area, but not so edgy as to scare away my corporate clients.
Sub text should read Photography, Video, Design
There also needs to be room for phone number and email.

```html
<!DOCTYPE html>
<html lang="en">
<head>
<meta charset="utf-8">
<title>Martin Coldwell Creative – Business Card</title>
<link href="https://fonts.googleapis.com/css2?family=Raleway:wght@400;600&display=swap" rel="stylesheet">
<style>
  :root {
    --stage: #ecebe8;
    --paper: #ffffff;
    --ink: #54575b;
    --charcoal: #55585c;
    --blue: #3ba4d6;
    --blue-deep: #2a78a8;
    --white: #ffffff;
  }
  * { box-sizing: border-box; margin: 0; padding: 0; }
  html, body { width: 1200px; height: 676px; overflow: hidden; }
  body {
    background: var(--stage);
    font-family: "Raleway", sans-serif;
    display: flex;
    align-items: center;
    justify-content: center;
    gap: 60px;
  }
  .card {
    position: relative;
    width: 500px;
    height: 286px;
    overflow: hidden;
    box-shadow: 0 10px 28px rgba(0,0,0,.14);
  }

  /* Front */
  .card-front { background: var(--paper); }
  .brand {
    position: absolute;
    left: 44px;
    top: 40px;
    display: flex;
    align-items: center;
    gap: 12px;
    color: var(--blue);
    font-weight: 600;
    font-size: 22px;
    letter-spacing: .5px;
    line-height: 1.1;
  }
  .brand-dot {
    width: 14px; height: 14px;
    border-radius: 50%;
    background: var(--blue);
    flex: none;
  }
  .contact {
    position: absolute;
    left: 70px;
    top: 124px;
    color: var(--ink);
    font-size: 13px;
    line-height: 1.55;
  }
  .contact-name {
    color: var(--blue);
    font-weight: 600;
    font-size: 15px;
    margin-bottom: 2px;
  }
  .contact-line { display: flex; align-items: center; gap: 7px; }
  .contact-line svg { width: 11px; height: 11px; fill: none; stroke: var(--blue); stroke-width: 1.6; }
  .web-tab {
    position: absolute;
    right: 0;
    bottom: 30px;
    width: 210px;
    height: 22px;
    background: var(--blue);
    color: var(--white);
    font-size: 11px;
    font-weight: 600;
    display: flex;
    align-items: center;
    justify-content: center;
  }
  .services-band {
    position: absolute;
    left: 0; right: 0; bottom: 0;
    height: 30px;
    background: var(--charcoal);
    color: var(--white);
    font-size: 12px;
    display: flex;
    align-items: center;
    padding-left: 150px;
    letter-spacing: .3px;
  }

  /* Back */
  .card-back { background: linear-gradient(160deg, var(--blue) 0%, var(--blue-deep) 100%); }
  .back-circle { position: absolute; inset: 0; }
  .back-web {
    position: absolute;
    right: 40px;
    top: 96px;
    color: var(--white);
    font-size: 14px;
    font-weight: 600;
  }
  .back-brand {
    position: absolute;
    left: 60px;
    top: 150px;
    color: var(--blue);
    font-weight: 600;
    font-size: 24px;
    line-height: 1.15;
    letter-spacing: .5px;
  }
</style>
</head>
<body>

  <section class="card card-front">
    <div class="brand">
      <span class="brand-dot"></span>
      <span>MARTIN COLDWELL<br>CREATIVE</span>
    </div>

    <div class="contact">
      <p class="contact-name">Martin Coldwell</p>
      <p class="contact-line">
        <svg viewBox="0 0 12 12"><path d="M2 1.5l2 .3 1 2.4-1.3 1a6 6 0 0 0 3 3l1-1.3 2.4 1 .3 2c-5 .6-9-3.4-8.4-8.4z"/></svg>
        123.4870.519
      </p>
      <p class="contact-line">
        <svg viewBox="0 0 12 12"><rect x="1.5" y="1.5" width="9" height="9" rx="1"/><path d="M4 6h4"/></svg>
        123.4870.519
      </p>
      <p class="contact-line">
        <svg viewBox="0 0 12 12"><rect x="1" y="2.5" width="10" height="7" rx="1"/><path d="M1 3l5 4 5-4"/></svg>
        info@martincoldwell.com
      </p>
    </div>

    <div class="web-tab">www.martincoldwell.com</div>
    <div class="services-band">Photography • Video • Design</div>
  </section>

  <section class="card card-back">
    <svg class="back-circle" viewBox="0 0 500 286" preserveAspectRatio="none" aria-hidden="true">
      <circle cx="175" cy="300" r="225" fill="#55585c"/>
    </svg>
    <p class="back-web">www.martincoldwell.com</p>
    <p class="back-brand">MARTIN COLDWELL<br>CREATIVE</p>
  </section>

</body>
</html>
```